Electronic Refurbishment Warehouse needs a Website

We are looking for a clean, professional looking design with iconic imagery. Our main point we want to get across is that we will help clients save time, and money, and provide outstanding quality. Our logo can be found in the uploads section. This site is used to impress clients that we have a pre-existing relationship with. This site will be available for the public but it will not be used to advertise to the public or to drive traffic to it. The color scheme we are looking to stay with is blue, but that is not to say that everything should be a shade of blue. Last note, see site map below.

Site Map:

Home
Company
a. company overview
b. CEO letter
Services
a. Remanufacture & Refurbishment Services
1. Consumer Electronics
2. Cellular Phones
b.Reverse Logistics Management
c.Warranty Repair & Field Services
d.Quality Control & Assurance
e.Warehousing & Distribution
Careers
Contact Us
Updates

Project Deadline Extended
Reason: We want to allocate more time for designers to do what they do best.

Target Market(s)

Phone and TV Retailers that may have units that need to be refurbished. Example Vorelli, tradequay, qlm, etc.

Industry/Entity Type

Electronics

Requirements
Must have
• Home Page Slider.
Iconic imagery and navigation.
The ability to be put into the 960 Grid.

```html
<!DOCTYPE html>
<html lang="en">
<head>
<meta charset="utf-8">
<title>Kestrel group – Home</title>
<link href="https://fonts.googleapis.com/css2?family=Source+Sans+3:ital,wght@0,400;0,600;1,400&display=swap" rel="stylesheet">
<style>
:root{
  --blue:#1f86d3;
  --blue-dark:#0c5ea8;
  --blue-deep:#1d5f9c;
  --nav-top:#3a9fe4;
  --nav-bot:#0d6cbc;
  --ink:#333;
  --ink-soft:#555;
  --link:#2a6fb0;
  --cream:#fcfbf1;
  --paper:#f4f3ee;
  --hero:#f1f3f5;
  --footer:#2f6ea9;
  --footer-bar:#275d94;
  --btn:#2e5f95;
}
*{margin:0;padding:0;box-sizing:border-box}
html,body{width:840px;height:1200px;overflow:hidden}
body{font-family:"Source Sans 3",Arial,sans-serif;color:var(--ink);background:#fff;position:relative}
.abs{position:absolute}
.topline{top:0;left:0;width:840px;height:5px;background:var(--blue)}
.header{top:5px;left:0;width:840px;height:76px;background:var(--paper);border-bottom:2px solid #cfd9e3}
.brand{left:22px;top:26px;display:flex;align-items:center;gap:8px;font-size:22px;color:var(--blue);font-weight:600}
.brand-mark{width:24px;height:24px;background:var(--blue);border-radius:3px}
.account{right:50px;top:11px;font-size:10px;color:var(--blue-dark);letter-spacing:.3px}
.account span{margin:0 6px;color:#7a9cbf}
.nav{top:83px;left:0;width:840px;height:38px;background:linear-gradient(var(--nav-top),var(--nav-bot))}
.nav a{position:absolute;top:0;height:38px;line-height:36px;color:#fff;font-size:13px;text-decoration:none;text-align:center}
.nav a.sep{border-right:1px solid rgba(255,255,255,.35)}
.nav a.active{background:var(--blue-dark)}
.nav a.active::after{content:"";position:absolute;left:50%;bottom:0;margin-left:-5px;border:5px solid transparent;border-bottom-color:#fff}
.search{right:58px;top:91px;width:156px;height:18px;border-radius:9px;background:#fff;font-size:9px;color:#667;line-height:18px;padding-left:10px}
.search svg{position:absolute;right:8px;top:3px}
.hero{top:121px;left:0;width:840px;height:277px;background:var(--hero)}
.hero h1{left:28px;top:172px;font-size:23px;font-weight:400;color:var(--blue)}
.hero .copy{left:31px;top:206px;width:330px;font-size:10px;line-height:15px;color:var(--ink-soft)}
.hero .copy p{margin-bottom:6px}
.pill{left:28px;top:317px;width:142px;height:21px;border-radius:11px;background:var(--blue);color:#fff;font-size:9px;line-height:21px;text-align:center}
.slide{left:418px;top:145px;width:364px;height:216px;border:3px solid var(--blue);background:linear-gradient(135deg,#c23a2e,#7d8a8e 45%,#d9dcdc 70%,#8a8f8a);box-shadow:0 8px 8px -4px rgba(0,0,0,.3)}
.arrow{width:28px;height:30px;top:243px;background:var(--blue-deep);border-radius:50%;color:#fff;text-align:center;line-height:28px;font-size:18px}
.trio{top:398px;left:0;width:840px;height:233px;background:var(--cream)}
.col{top:398px;height:233px}
.col.div{border-right:1px solid #ddd9c4}
.col h2{position:absolute;top:20px;font-size:15px;font-weight:400;color:#222;white-space:nowrap}
.col .txt{position:absolute;top:48px;font-size:9.5px;line-height:14.8px;color:var(--link)}
.col .txt p{margin-bottom:5px}
.col ul{list-style:none;margin-top:12px}
.col li{position:relative;padding-left:13px;margin-bottom:5px;color:#444}
.col li::before{content:"";position:absolute;left:0;top:5px;width:5px;height:5px;background:var(--btn)}
.btn{position:absolute;top:194px;width:69px;height:22px;background:var(--btn);color:#fff;font-size:10px;line-height:22px;text-align:center;box-shadow:0 4px 4px -2px rgba(0,0,0,.3)}
.services-title{left:20px;top:664px;font-size:18px;color:var(--blue-dark)}
.svc{width:240px}
.svc .ico{position:absolute;left:0;top:0;width:38px;height:38px;border-radius:6px}
.svc .t{position:absolute;left:52px;top:0;width:194px;font-size:9.5px;line-height:14.5px;color:var(--link)}
.svc .t b{font-weight:400;color:#222}
.svc .more{position:absolute;left:53px;top:72px;font-style:italic;font-size:11px;color:#333}
.hsep{height:1px;background:linear-gradient(90deg,transparent,#ccc 30%,#ccc 70%,transparent)}
.vsep{width:1px;background:linear-gradient(transparent,#ccc 30%,#ccc 70%,transparent)}
.news-title{left:599px;top:686px;font-size:15px;color:#222}
.news{left:599px;width:210px}
.news .t{position:absolute;left:46px;top:0;font-size:10.5px;color:var(--blue);white-space:nowrap}
.news .d{position:absolute;left:46px;top:13px;width:170px;font-size:9px;line-height:12.5px;color:#555}
.news-read{left:600px;top:923px;font-size:11px;color:#222}
.footer{top:961px;left:0;width:840px;height:196px;background:linear-gradient(#3a78b3,var(--footer))}
.fcol{top:978px;color:#fff}
.fcol h3{font-size:12px;font-weight:400;padding-bottom:8px;border-bottom:1px solid rgba(255,255,255,.2);margin-bottom:8px;white-space:nowrap}
.fcol li{list-style:none;font-size:9px;line-height:19.5px;color:#e8f0f8;white-space:nowrap}
.social{display:flex;gap:4px;margin:4px 0 12px}
.social span{width:17px;height:17px;border-radius:3px;background:#5fa2e0;border:1px solid #9cc6ee}
.fbar{top:1157px;left:0;width:840px;height:43px;background:var(--footer-bar);color:#fff;font-size:9px;line-height:40px;padding-left:30px}
</style>
</head>
<body>
<div class="abs topline"></div>
<header class="abs header"></header>
<div class="abs brand"><span class="brand-mark"></span>Kestrel group</div>
<div class="abs account">REGISTER<span>|</span>LOG IN<span>|</span>SIGN UP</div>

<nav class="abs nav">
  <a class="active" style="left:18px;width:84px">Home</a>
  <a class="sep" style="left:102px;width:116px">Company</a>
  <a class="sep" style="left:218px;width:105px">Services</a>
  <a class="sep" style="left:323px;width:99px">Careers</a>
  <a style="left:422px;width:118px">Contact us</a>
</nav>
<div class="abs search">search here..
  <svg width="14" height="11" viewBox="0 0 14 11"><circle cx="5" cy="5" r="3.5" fill="none" stroke="#999" stroke-width="1.5"/><line x1="7.5" y1="7" x2="12" y2="10" stroke="#999" stroke-width="2"/></svg>
</div>

<section class="abs hero"></section>
<h1 class="abs" style="left:28px;top:172px;font-size:23px;font-weight:400;color:var(--blue)">KESTREL GROUP HEADLINE SERVICES</h1>
<div class="abs" style="left:31px;top:206px;width:330px;font-size:10px;line-height:15px;color:var(--ink-soft)">
  <p style="margin-bottom:6px">Brightlane eSolutions is a professional website design company dedicated to provide excellent services. We at Brightlane eSolutions think graphic design as a combination and collaboration of ideas and technology.</p>
  <p>Our Website Design team give an unforgettable impression on the customers and the clients. We can assure you that this is the best place for requirement of yours regarding website design solutions</p>
</div>
<div class="abs pill">CLICK HERE TO READ MORE</div>
<div class="abs slide" role="img" aria-label="Photo of a technician testing a circuit breaker panel with coloured wiring"></div>
<div class="abs arrow" style="left:392px">&#8249;</div>
<div class="abs arrow" style="left:781px">&#8250;</div>

<section class="abs trio"></section>
<div class="abs col div" style="left:0;width:279px">
  <h2 style="left:18px">WELCOME TO OUR WEBSITE..</h2>
  <div class="txt" style="left:21px;width:240px">
    <p>Brightlane eSolutions is a web service company, offering a wide range of services which range from designing and development, that is covering almost all the fields in the best possible way.</p>
    <p>To be the best we know what and how to present beautifully the working of the client's need and their advantages be highlighted. We act in accordance with the Industry certified processes to deliver the best to our clients all over</p>
  </div>
  <div class="btn" style="left:22px">READ MORE</div>
</div>
<div class="abs col div" style="left:279px;width:271px">
  <h2 style="left:24px">ABOUT OUR COMPANY</h2>
  <div class="txt" style="left:25px;width:225px">
    <p>Brightlane eSolutions is a web service company, offering a wide range of services which range from designing and development</p>
    <ul>
      <li>Design company dedicated to excellent</li>
      <li>Dedicated to provide excellent services</li>
      <li>Design company dedicated to provide excellent</li>
      <li>Dedicated to provide excellent services</li>
    </ul>
  </div>
  <div class="btn" style="left:23px">READ MORE</div>
</div>
<div class="abs col" style="left:550px;width:290px">
  <h2 style="left:22px">KESTREL GROUP HEADLINE HERE</h2>
  <div class="txt" style="left:23px;width:235px">
    Brightlane eSolutions is a web service company, offering a wide range of services which range from designing and development, that is covering almost all the fields in the best possible way.<br>
    Brightlane eSolutions is a professional website design company dedicated to provide excellent services. We at Brightlane eSolutions think graphic design as a combination and collaboration of ideas and technology. Our Website Design team give an unforgettable impression
  </div>
  <div class="btn" style="left:23px">READ MORE</div>
</div>

<h2 class="abs services-title" style="font-weight:400">Some of Our Services here</h2>
<div class="abs vsep" style="left:289px;top:695px;height:250px"></div>
<div class="abs hsep" style="left:30px;top:802px;width:530px"></div>

<div class="abs svc" style="left:21px;top:706px">
  <div class="ico" role="img" aria-label="Magnifier over document icon" style="background:linear-gradient(#e8ecef,#b8c4cc)"></div>
  <div class="t"><b>Brightlane eSolutions is a web service</b> The only way to success is through the right path and that's what we provide you. None of the other companies has the result we do.</div>
  <div class="more">click here to read more..</div>
</div>
<div class="abs svc" style="left:294px;top:706px">
  <div class="ico" role="img" aria-label="Globe icon" style="border-radius:50%;background:radial-gradient(circle at 40% 35%,#bfe3fb,#2d87cf)"></div>
  <div class="t"><b>Brightlane eSolutions is a web service</b> The only way to success is through the right path and that's what we provide you. None of the other companies has the result we do.</div>
  <div class="more">click here to read more..</div>
</div>
<div class="abs svc" style="left:21px;top:826px">
  <div class="ico" role="img" aria-label="Toolbox icon" style="background:linear-gradient(#f3c94a,#d9952a)"></div>
  <div class="t"><b>Brightlane eSolutions is a web service</b> The only way to success is through the right path and that's what we provide you. None of the other companies has the result we do.</div>
  <div class="more" style="top:67px">click here to read more..</div>
</div>
<div class="abs svc" style="left:295px;top:826px">
  <div class="ico" role="img" aria-label="House with tools icon" style="background:linear-gradient(#d9523f,#9aa7b3)"></div>
  <div class="t"><b>Brightlane eSolutions is a web service</b> The only way to success is through the right path and that's what we provide you. None of the other companies has the result we do.</div>
  <div class="more" style="top:69px">click here to read more..</div>
</div>

<h2 class="abs news-title" style="font-weight:400">Latest News &amp; Updates</h2>
<div class="abs news" style="top:730px">
  <svg width="34" height="34" viewBox="0 0 34 34"><rect x="1" y="4" width="32" height="29" rx="2" fill="#f2f2f2" stroke="#bbb"/><rect x="1" y="4" width="32" height="9" fill="#c9433a"/><text x="6" y="23" font-size="8" font-family="Arial" fill="#555">12</text></svg>
  <div class="t">TOPIC GOES HERE</div>
  <div class="d">Brightlane eSolutions is a web service company, offering a wide</div>
</div>
<div class="abs hsep" style="left:599px;top:781px;width:210px"></div>
<div class="abs news" style="top:795px">
  <svg width="34" height="34" viewBox="0 0 34 34"><rect x="1" y="4" width="32" height="29" rx="2" fill="#f2f2f2" stroke="#bbb"/><rect x="1" y="4" width="32" height="9" fill="#c9433a"/><text x="6" y="23" font-size="8" font-family="Arial" fill="#555">12</text></svg>
  <div class="t">TOPIC GOES HERE</div>
  <div class="d">Brightlane eSolutions is a web service company, offering a wide</div>
</div>
<div class="abs hsep" style="left:599px;top:848px;width:210px"></div>
<div class="abs news" style="top:864px">
  <svg width="34" height="34" viewBox="0 0 34 34"><rect x="1" y="4" width="32" height="29" rx="2" fill="#f2f2f2" stroke="#bbb"/><rect x="1" y="4" width="32" height="9" fill="#c9433a"/><text x="6" y="23" font-size="8" font-family="Arial" fill="#555">12</text></svg>
  <div class="t">TOPIC GOES HERE</div>
  <div class="d">Brightlane eSolutions is a web service company, offering a wide</div>
</div>
<div class="abs news-read">READ MORE</div>

<footer class="abs footer"></footer>
<div class="abs fcol" style="left:39px;width:110px">
  <h3>COMPANY</h3>
  <ul><li>Main Page</li><li>Company &nbsp;Overview</li><li>Services List</li><li>Careers</li><li>Contact Us</li></ul>
</div>
<div class="abs fcol" style="left:165px;width:190px">
  <h3>OUR SERVICES</h3>
  <ul><li>Remanufacture &amp; Refurbishment Services</li><li>Reverse Logistics Management</li><li>Warranty Repair &amp; Field Services</li><li>Quality Control &amp; Assurance</li><li>Warehousing &amp; Distribution</li></ul>
</div>
<div class="abs fcol" style="left:378px;width:150px">
  <h3>SUPPORT &amp; FAQ</h3>
  <ul><li>Featued Products</li><li>Testimonials</li><li>FAQ</li><li>SUpport</li></ul>
</div>
<div class="abs fcol" style="left:558px;width:220px">
  <h3>CONNECT WITH US</h3>
  <div class="social"><span></span><span></span><span></span><span></span></div>
  <ul><li>Friendline &nbsp;| &nbsp;Searchly &nbsp;| &nbsp;Chirpnet &nbsp;| &nbsp;Worklink</li></ul>
</div>
<div class="abs fbar">Copyright © 2012 Company Name &nbsp;| &nbsp;All right reserved</div>
</body>
</html>
```